Maple Vital App Landing Page

Looking for a landing page for our app at maplevitalco.com

Target Market(s)

Health care facilities

Industry/Entity Type

Healthcare

Number of Pages Required

1 page

```html
<!DOCTYPE html>
<html lang="en">
<head>
<meta charset="utf-8">
<title>Maple Vital – Covid-19 Screening App</title>
<link href="https://fonts.googleapis.com/css2?family=Poppins:wght@300;400;500;600;700;800&family=Courier+Prime:wght@400;700&display=swap" rel="stylesheet">
<style>
:root{
  --blue:#0b78e6;
  --blue-deep:#0866d8;
  --cyan:#25c2e2;
  --teal:#12909f;
  --coral:#ff5a3d;
  --white:#ffffff;
  --ink:#1c2230;
  --grey:#9aa3ad;
}
*{margin:0;padding:0;box-sizing:border-box}
html,body{width:1200px;height:844px;overflow:hidden}
body{font-family:'Poppins',sans-serif;color:var(--white);background:var(--blue)}
.page{position:relative;width:1200px;height:844px;overflow:hidden;
  background:linear-gradient(120deg,#0b6fe0 0%,#0a86ea 45%,#16a6e6 100%)}
.backdrop{position:absolute;inset:0}
.glow{position:absolute;border-radius:50%;filter:blur(30px);opacity:.35}

.header{position:absolute;left:0;top:0;width:100%;height:100px}
.brand{position:absolute;left:67px;top:38px;display:flex;align-items:center;gap:10px;
  font-size:27px;font-weight:400;letter-spacing:.3px;text-transform:uppercase}
.brand-dot{width:22px;height:22px;border-radius:50%;border:2px solid var(--white)}
.nav{position:absolute;top:44px;display:flex;font-size:14px;font-weight:500;letter-spacing:.2px}
.nav a{color:var(--white);text-decoration:none;position:absolute;white-space:nowrap}
.login{position:absolute;left:1035px;top:29px;width:98px;height:46px;background:var(--white);
  color:var(--ink);border-radius:23px 0 23px 23px;font-size:15px;font-weight:600;
  display:flex;align-items:center;justify-content:center}

.hero{position:absolute;left:66px;top:282px}
.hero-kicker{font-size:23px;font-weight:600}
.hero-title{margin-top:4px;line-height:.86}
.hero-title .light{display:block;font-size:60px;font-weight:300;letter-spacing:1px}
.hero-title .bold{display:block;font-size:60px;font-weight:800;letter-spacing:.5px}
.hero-copy{margin-top:22px;margin-left:2px;font-size:14.5px;line-height:20px;font-weight:400;width:390px}
.cta{position:absolute;left:67px;top:504px;width:210px;height:52px;background:var(--coral);
  border-radius:26px 0 26px 26px;font-size:14.5px;font-weight:600;display:flex;
  align-items:center;justify-content:center;letter-spacing:.3px}
.copyright{position:absolute;left:68px;top:802px;font-size:13px;font-weight:500}

.phone{position:absolute;background:var(--white);border-radius:38px;overflow:hidden;
  transform:rotate(25deg);box-shadow:0 20px 40px rgba(0,40,120,.18)}
.phone-bar{height:92px;color:var(--white);text-align:center;padding-top:36px;position:relative;
  border-radius:0 0 0 0}
.phone-bar::before{content:"";position:absolute;left:50%;top:12px;width:30px;height:4px;margin-left:-22px;
  background:var(--white);border-radius:2px}
.phone-bar::after{content:"";position:absolute;left:50%;top:11px;width:6px;height:6px;margin-left:14px;
  background:var(--white);border-radius:50%}
.bar-title{font-size:11px;font-weight:500;text-transform:uppercase;letter-spacing:.5px}
.bar-sub{font-size:5px;text-transform:uppercase;letter-spacing:.5px;opacity:.9}
.bar-icon{position:absolute;top:36px;font-size:11px}
.bar-icon.back{left:14px}.bar-icon.close{right:14px}
.curve{position:absolute;left:0;bottom:-1px;width:100%;height:20px}

.admin{left:620px;top:235px;width:205px;height:372px}
.admin .phone-bar{background:var(--teal)}
.admin .body{padding:6px 18px;font-family:'Courier Prime',monospace;color:var(--teal);font-size:9.5px;line-height:11px}
.admin h4{text-align:center;color:#0a4650;font-size:10.5px;margin-bottom:6px}
.field{border-bottom:1px solid var(--teal);font-family:'Poppins',sans-serif;font-size:7px;padding:4px 0 1px;margin-top:4px}
.boxfield{border:1px solid var(--teal);border-radius:4px;height:18px;font-family:'Poppins',sans-serif;font-size:5.5px;padding:4px 6px;margin-top:8px;width:78%;display:inline-block}
.done{display:inline-block;width:17%;margin-left:3%;height:16px;background:#8fcbd2;border-radius:3px;font-family:'Poppins',sans-serif;font-size:5px;color:#fff;text-align:center;line-height:16px}

.welcome{left:870px;top:148px;width:205px;height:400px}
.welcome .phone-bar{background:var(--blue)}
.welcome .body{text-align:center;color:var(--blue);padding-top:14px}
.screen-brand{font-size:17px;font-weight:600;text-transform:uppercase;display:flex;justify-content:center;align-items:center;gap:6px}
.screen-brand i{width:10px;height:10px;border-radius:50%;border:1.5px solid var(--blue)}
.tagline{font-size:6px;color:#5a8fd6}
.art{margin:14px auto 0;width:150px;height:110px;border-radius:14px;
  background:linear-gradient(135deg,#e6f0fd,#c7ddfa 60%,#5d90e6)}
.wide-btn{margin:34px auto 0;width:150px;height:18px;background:var(--blue);border-radius:3px;
  color:#fff;font-size:5.5px;display:flex;justify-content:space-between;align-items:center;padding:0 8px}

.triage{left:752px;top:525px;width:205px;height:400px}
.triage .phone-bar{background:var(--coral)}
.triage .body{padding:4px 20px;text-align:center;color:var(--coral)}
.note{font-size:7.5px;line-height:10px}
.lbl{font-size:6.5px;margin-top:14px}
.input{border:1px solid var(--coral);border-radius:3px;height:20px;margin-top:3px;font-size:5.5px;color:#888;text-align:left;padding:5px 6px}
.coral-btn{margin-top:16px;height:20px;background:var(--coral);border-radius:3px;color:#fff;font-size:5.5px;display:flex;justify-content:space-between;align-items:center;padding:0 8px}

.role{left:1010px;top:395px;width:205px;height:400px}
.role .phone-bar{background:var(--blue)}
.role .body{padding:10px 18px;text-align:center;color:var(--blue)}
.q{font-size:7px;margin-bottom:6px}
.tiles{display:grid;grid-template-columns:1fr 1fr;gap:6px}
.tile{height:44px;border:1px solid var(--blue);border-radius:4px;font-size:6px;text-transform:uppercase;
  display:flex;flex-direction:column;align-items:center;justify-content:center;gap:4px}
.tile.on{background:var(--blue);color:#fff}
.tile svg{width:12px;height:12px}
.q2{font-size:7px;margin:12px 0 4px}
.select{border:1px solid var(--blue);border-radius:3px;height:20px;font-size:5.5px;text-align:left;padding:5px 6px;color:#333}
.blue-btn{margin-top:10px;height:20px;background:var(--blue);border-radius:3px;color:#fff;font-size:5.5px;display:flex;justify-content:space-between;align-items:center;padding:0 8px}

.user-card{position:absolute;background:var(--white);color:var(--ink)}
.user-card .name{font-size:14px;font-weight:600;text-transform:uppercase;line-height:16px}
.user-card .tag{font-size:12px;color:var(--grey);text-transform:uppercase;line-height:14px}
.card-left{left:581px;top:693px;width:141px;height:64px;border-radius:8px 0 0 8px;display:flex;align-items:center;gap:10px;padding-left:18px}
.avatar{width:36px;height:36px;border-radius:50%;background:linear-gradient(135deg,#cfe6ef,#7fb6c8)}
.card-right{left:1117px;top:302px;width:90px;height:66px;border-radius:8px 0 0 8px;padding:30px 0 0 14px}
.avatar-sq{position:absolute;left:19px;top:-17px;width:38px;height:38px;border-radius:6px;background:linear-gradient(135deg,#b9d6e6,#5f8ea5)}
</style>
</head>
<body>
<div class="page">
  <svg class="backdrop" width="1200" height="844" viewBox="0 0 1200 844" aria-hidden="true">
    <defs>
      <linearGradient id="wave" x1="0" y1="0" x2="1" y2="1">
        <stop offset="0" stop-color="#1aa8e8"/>
        <stop offset="1" stop-color="#2bc6e2"/>
      </linearGradient>
    </defs>
    <path d="M560 0 C600 120 640 170 700 250 C760 330 700 420 640 520 C580 620 520 720 540 844 L1200 844 L1200 0 Z" fill="url(#wave)" opacity=".85"/>
    <path d="M545 0 C590 90 660 150 760 180 C880 215 980 140 1060 0 Z" fill="#0a7fe8" opacity=".55"/>
    <circle cx="0" cy="670" r="60" fill="#23b7e4" opacity=".6"/>
    <circle cx="605" cy="390" r="50" fill="#2bc6e2" opacity=".5"/>
  </svg>
  <div class="glow" style="left:160px;top:150px;width:260px;height:220px;background:#3fa9f5"></div>
  <div class="glow" style="left:330px;top:560px;width:230px;height:200px;background:#3fa9f5"></div>

  <header class="header">
    <div class="brand"><span class="brand-dot"></span>Maple Vital</div>
    <nav class="nav">
      <a style="left:711px">WHY PAYMENT APP</a>
      <a style="left:872px">ABOUT US</a>
      <a style="left:974px">PRICES</a>
    </nav>
    <div class="login">LOGIN</div>
  </header>

  <section class="hero">
    <p class="hero-kicker">Start your</p>
    <h1 class="hero-title"><span class="light">Covid-19</span><span class="bold">Screening Now</span></h1>
    <p class="hero-copy">Lorem ipsum dolor sit ametut labore et dolore Quis ipsum suspendisse ultrices</p>
  </section>
  <div class="cta">DOWNLOAD THE APP</div>

  <div class="phone admin">
    <div class="phone-bar"><span class="bar-icon back">‹</span><div class="bar-title">Covid-19 Admin Screen</div><div class="bar-sub">Admin screen - vendor exception</div><span class="bar-icon close">×</span></div>
    <div class="body">
      <h4>Vendor Exception</h4>
      <p>In an effort to minimize exposure risk to all of our residents, we are restricting vendors from entering the facility. Thank you for completing this screening process.</p>
      <p style="margin-top:6px">I, Name/Title ______, am employed by Entity ______, and request an essential visit for the following reason(s): Reason(s) ______. I am attesting that my visit is necessary and imminent in nature.</p>
      <div class="field">Entity Phone Number</div>
      <div class="field">Entity email</div>
      <div class="boxfield">Sign with initials</div><span class="done">Done</span>
    </div>
  </div>

  <div class="phone welcome">
    <div class="phone-bar"><div class="bar-title">Covid-19 Screening</div><div class="bar-sub">Screening - welcome</div></div>
    <div class="body">
      <div class="screen-brand"><i></i>Maple Vital</div>
      <div class="tagline">Keeping you safe.</div>
      <div class="art" role="img" aria-label="Illustration of visitors wearing masks walking apart"></div>
      <div class="wide-btn"><span>Start your COVID-19 screening now</span><span>›</span></div>
    </div>
  </div>

  <div class="phone triage">
    <div class="phone-bar"><span class="bar-icon back">‹</span><div class="bar-title">Covid-19 Triage</div><div class="bar-sub">Triage - temperature</div><span class="bar-icon close">×</span></div>
    <div class="body">
      <p class="note">Please go to reception desk for a temperature reading</p>
      <p class="lbl">Temperature</p><div class="input">98.6°F</div>
      <p class="lbl">Nurse ID</p><div class="input">####</div>
      <div class="coral-btn"><span>Next</span><span>›</span></div>
    </div>
  </div>

  <div class="phone role">
    <div class="phone-bar"><span class="bar-icon back">‹</span><div class="bar-title">Covid-19 Screening</div><div class="bar-sub">Screening - staff</div></div>
    <div class="body">
      <p class="q">Who are you?</p>
      <div class="tiles">
        <div class="tile"><svg viewBox="0 0 12 12"><rect x="1" y="2" width="10" height="8" rx="1" fill="none" stroke="currentColor"/><circle cx="4" cy="6" r="1.4" fill="currentColor"/></svg>Staff</div>
        <div class="tile"><svg viewBox="0 0 12 12"><circle cx="6" cy="4" r="2.2" fill="currentColor"/><path d="M2 11c0-3 8-3 8 0z" fill="currentColor"/></svg>Provider</div>
        <div class="tile on"><svg viewBox="0 0 12 12"><circle cx="6" cy="4" r="2.2" fill="currentColor"/><path d="M2 11c0-3 8-3 8 0z" fill="currentColor"/></svg>Visitor</div>
        <div class="tile"><svg viewBox="0 0 12 12"><circle cx="6" cy="4" r="2.2" fill="currentColor"/><path d="M2 11c0-3 8-3 8 0z" fill="currentColor"/></svg>Vendor</div>
      </div>
      <p class="q2">Which facility are you at?</p>
      <div class="select">Harbor View Clinic</div>
      <div class="blue-btn"><span>Next</span><span>›</span></div>
    </div>
  </div>

  <div class="user-card card-left">
    <div class="avatar" role="img" aria-label="Portrait photo of a masked visitor"></div>
    <div><p class="name">Covid 19</p><p class="tag">Covid 19</p></div>
  </div>
  <div class="user-card card-right">
    <div class="avatar-sq" role="img" aria-label="Portrait photo of a masked user"></div>
    <p class="name">Dana R</p><p class="tag">Covid 19</p>
  </div>

  <p class="copyright">© COPYRIGHT 2020 ALL RIGHT RESERVED</p>
</div>
</body>
</html>
```